Vantor Medica Innovative Business Card

Stunning business card. Background will be black. Letters in gold. Modern yet simple design that is attention grabbing. QR code leading to site. Attractive primarily to males ages 30 to 50 but also to females in same age range looking for beauty and mental health products

Target Market(s)

Males in the 30-50 age demographics

Industry/Entity Type

Pharmaceuticals selling erectile dysfunction and mens health medications

Contact Information for Business Card

www.vantormedica.example; (775) BUY-KELO; info@vantormedica.example

Colors
FFC000
F8CF3A
FAE287
FDF2CF
FEFAEE

Requirements
Must have
• Black business card with gold letters.
Nice to have
• perhaps just the logo or the "R" icon by itself on one side
Should not have
• too much content so it does not look busy

```html
<!DOCTYPE html>
<html lang="en">
<head>
<meta charset="utf-8">
<title>Vantor Medica — Business Card</title>
<link rel="stylesheet" href="https://fonts.googleapis.com/css2?family=Montserrat:wght@700;800&family=Arimo:wght@400&display=swap">
<style>
  :root {
    --page: #161616;
    --card: #262626;
    --gold: #d6ab33;
    --text: #f2f2f2;
    --rule: #d9d9d9;
    --emboss-dark: #0e0e0e;
    --emboss-mid: #1c1c1c;
    --emboss-light: #464646;
  }
  * { box-sizing: border-box; margin: 0; padding: 0; }
  html, body { width: 1200px; height: 963px; overflow: hidden; }
  body {
    background: var(--page);
    display: flex;
    flex-direction: column;
    align-items: center;
    justify-content: center;
    gap: 56px;
  }
  .card {
    width: 700px;
    height: 400px;
    border-radius: 26px;
    background: radial-gradient(circle at 55% 50%, #2c2c2c 0%, var(--card) 60%, #222 100%);
    box-shadow: 0 0 0 2px var(--gold), 0 18px 40px rgba(0,0,0,.55);
    position: relative;
    overflow: hidden;
  }
  /* front */
  .card-front {
    display: flex;
    align-items: center;
    padding: 0 56px 0 70px;
  }
  .brand {
    width: 250px;
    display: flex;
    align-items: center;
    gap: 14px;
  }
  .brand-dot {
    width: 22px; height: 22px;
    border-radius: 50%;
    background: var(--gold);
    flex: none;
  }
  .brand-name {
    font-family: "Montserrat", sans-serif;
    font-weight: 800;
    font-size: 30px;
    line-height: 1.05;
    color: var(--gold);
    text-transform: uppercase;
    letter-spacing: 0.5px;
  }
  .divider {
    width: 1px;
    height: 170px;
    background: var(--rule);
    margin: 0 34px 0 20px;
    flex: none;
  }
  .details { font-family: "Arimo", sans-serif; color: var(--text); }
  .person-name {
    font-family: "Montserrat", sans-serif;
    font-weight: 800;
    font-size: 22px;
    color: var(--gold);
    text-transform: uppercase;
    letter-spacing: 0.5px;
  }
  .person-role { font-size: 16px; margin: 2px 0 18px; }
  .contact-list { list-style: none; }
  .contact-list li {
    display: flex;
    align-items: center;
    gap: 10px;
    font-size: 16px;
    line-height: 1.75;
  }
  .contact-list svg { width: 15px; height: 15px; flex: none; }
  /* back */
  .card-back { padding: 40px 48px; }
  .card-back .brand { width: auto; position: relative; z-index: 1; }
  .card-back .brand-name { font-size: 50px; }
  .card-back .brand-dot { width: 32px; height: 32px; }
  .emblem-area {
    position: absolute;
    left: 150px;
    top: 140px;
    width: 600px;
    height: 300px;
    border-radius: 40px;
    background: linear-gradient(160deg, var(--emboss-dark) 0%, var(--emboss-mid) 55%, var(--emboss-light) 100%);
    box-shadow: inset 0 2px 6px rgba(0,0,0,.6), 0 1px 0 rgba(255,255,255,.05);
  }
</style>
</head>
<body>

  <section class="card card-front" aria-label="Business card front">
    <div class="brand">
      <span class="brand-dot"></span>
      <span class="brand-name">Vantor<br>Medica</span>
    </div>
    <div class="divider"></div>
    <div class="details">
      <h1 class="person-name">Marcus Hale</h1>
      <p class="person-role">Manager</p>
      <ul class="contact-list">
        <li>
          <svg viewBox="0 0 16 16" aria-hidden="true"><path fill="var(--gold)" d="M3.6 1.5l2.3 2.8-1.3 1.6c.9 2 2.5 3.6 4.5 4.5l1.6-1.3 2.8 2.3-1.4 2.3C7 13.6 2.4 9 2.3 3l1.3-1.5z"/></svg>
          (775) BUY-KELO
        </li>
        <li>
          <svg viewBox="0 0 16 16" aria-hidden="true"><rect x="1" y="3" width="14" height="10" rx="1" fill="var(--gold)"/><path d="M1.5 3.6L8 9l6.5-5.4" stroke="#262626" stroke-width="1.3" fill="none"/></svg>
          info@vantormedica.example
        </li>
        <li>
          <svg viewBox="0 0 16 16" aria-hidden="true"><circle cx="8" cy="8" r="6.5" fill="none" stroke="var(--gold)" stroke-width="1.6"/><path d="M1.5 8h13M8 1.5c-3 3.5-3 9.5 0 13M8 1.5c3 3.5 3 9.5 0 13" stroke="var(--gold)" stroke-width="1.2" fill="none"/></svg>
          www.vantormedica.example
        </li>
      </ul>
    </div>
  </section>

  <section class="card card-back" aria-label="Business card back">
    <div class="brand">
      <span class="brand-dot"></span>
      <span class="brand-name">Vantor Medica</span>
    </div>
    <div class="emblem-area" role="img" aria-label="Large embossed brand emblem in dark tones, bleeding off the lower right edge"></div>
  </section>

</body>
</html>
```